make a fireworks website

we are manufacturer of fireworks in Asia.
we need a HD fireworks website for showing product to all world customers.
we also need an register for member system,location, forum,products..etc
I added my Logo for the company.
brightnova.com.hk

and please message me if you have
any question.
here some example of website:
http://www.skyplumeshow.com/
http://www.tornelupyro.com/
http://www.quarvel-pyro.co.uk/
http://www.mirethpyro.co.uk/

```html
<!DOCTYPE html>
<html lang="en">
<head>
<meta charset="utf-8">
<title>BrightNova Fireworks</title>
<link rel="stylesheet" href="https://fonts.googleapis.com/css2?family=Montserrat:wght@400;600;700&family=Roboto+Slab:wght@300;400&display=swap">
<style>
:root{
  --coral:#f26d68;
  --coral-soft:rgba(242,109,104,.88);
  --ink:#333;
  --text:#555;
  --muted:#8a8a8a;
  --band:#eeeeee;
  --grey-band:#b4b4b4;
  --line:#dddddd;
  --white:#fff;
}
*{box-sizing:border-box;margin:0;padding:0}
html,body{width:1200px;height:2274px;overflow:hidden}
body{font-family:"Montserrat",sans-serif;color:var(--text);background:var(--white);position:relative}
.wrap{position:relative;width:937px;margin:0 auto}
a{color:inherit;text-decoration:none}
ul{list-style:none}

/* header */
.site-header{height:100px;background:var(--white)}
.site-header .wrap{height:100px;display:flex;align-items:center;justify-content:space-between}
.brand{display:flex;align-items:center;gap:12px;margin-left:32px;font-family:"Montserrat",sans-serif;font-weight:700;font-size:26px;color:var(--coral)}
.brand-dot{width:26px;height:26px;border-radius:50%;background:var(--coral)}
.main-nav{display:flex;align-items:center;gap:36px;margin-right:62px;font-size:13px;font-weight:700;letter-spacing:1.5px;color:var(--ink)}
.btn-signin{background:var(--coral);color:var(--white);padding:10px 20px}

/* sub navigation */
.subnav{height:47px;background:#f2f2f2;border-top:1px solid #e4e4e4;border-bottom:1px solid #e4e4e4}
.subnav .wrap{height:47px;display:flex;align-items:center;justify-content:space-between}
.subnav-links{display:flex;gap:30px;font-size:12px;letter-spacing:1px;color:var(--ink)}
.social{display:flex;gap:8px}
.social span{width:20px;height:20px;background:#c8c8c8;border-radius:2px;display:block}

/* hero */
.hero{height:470px;position:relative;background:linear-gradient(180deg,#2a2145 0%,#5b3f6d 35%,#7a4a63 60%,#3b2b3a 85%,#1d1820 100%)}
.hero-box{position:absolute;left:0;top:109px;width:562px;height:256px;background:var(--coral-soft);padding:30px 28px}
.hero-kicker{font-size:10px;letter-spacing:2px;color:#fde3e1}
.hero-title{font-family:"Roboto Slab",serif;font-weight:300;font-size:38px;color:var(--white);margin:12px 0 10px}
.hero-text{font-size:19px;line-height:1.35;color:#fde3e1;width:500px}
.hero-actions{display:flex;gap:8px;margin-top:20px}
.btn-light{background:var(--white);color:var(--coral);font-size:11px;font-weight:700;letter-spacing:1.5px;padding:11px 18px;border:1px solid var(--white)}
.btn-outline{border:1px solid var(--white);color:var(--white);font-size:11px;font-weight:700;letter-spacing:1.5px;padding:11px 18px}
.hero-dots{position:absolute;left:0;right:0;top:431px;display:flex;justify-content:center;gap:8px}
.hero-dots span{width:13px;height:13px;border-radius:50%;border:2px solid #ddd}
.hero-dots span.on{background:#ddd}

/* features */
.features{height:288px;background:var(--grey-band)}
.features .wrap{display:flex;justify-content:space-between;padding:40px 40px 0}
.feature{width:250px;text-align:center}
.feature-icon{width:82px;height:82px;margin:0 auto 10px;border-radius:6px}
.feature h3{font-family:"Roboto Slab",serif;font-weight:400;font-size:17px;color:var(--white)}
.feature .rule{width:50px;height:2px;background:var(--coral);margin:10px auto 16px}
.feature p{font-size:12px;line-height:1.6;color:#e6e6e6}
.feature .more{display:block;margin-top:20px;font-size:10px;font-weight:700;letter-spacing:2px;color:var(--coral)}

/* blog */
.blog-area{height:357px;background:var(--band)}
.blog-area .wrap{display:flex;padding-top:30px}
.blog-col{width:617px}
.section-label{font-size:16px;font-weight:700;color:var(--ink);display:flex;align-items:center;gap:10px;margin-bottom:16px}
.plus{width:16px;height:16px;border-radius:50%;background:var(--coral)}
.post-list{background:var(--white)}
.post-list li{height:50px;display:flex;align-items:center;justify-content:space-between;padding:0 26px;border-bottom:1px solid var(--band);font-size:15px;color:var(--coral)}
.post-list li::after{content:"";width:14px;height:14px;border-radius:50%;background:#d0d0d0}
.cat-col{margin-left:27px;padding-top:0}
.cat-col h4{font-family:"Roboto Slab",serif;font-weight:400;font-size:17px;color:var(--ink);margin-bottom:18px}
.cat-col li{font-size:12px;line-height:25px;font-weight:600;color:#777}
.cat-col li small{font-weight:400;color:#aaa}

/* projects */
.projects{height:452px;text-align:center;padding-top:36px}
.projects h2{font-family:"Roboto Slab",serif;font-weight:400;font-size:30px;color:var(--ink)}
.projects .rule{width:84px;height:2px;background:var(--coral);margin:12px auto 0}
.project-strip{display:flex;margin-top:22px;border-top:3px solid var(--coral);border-bottom:3px solid var(--coral)}
.project-tile{flex:1;height:152px}
.tile-a{background:radial-gradient(circle at 50% 50%,#b9b4a8 0%,#4a4442 35%,#141213 75%)}
.tile-b{background:radial-gradient(circle at 50% 45%,#b43a33 0%,#5b1e1c 40%,#141010 80%)}
.projects p{font-size:15px;line-height:1.8;color:var(--text);width:790px;margin:26px auto 0}
.btn-frame{display:inline-block;margin-top:24px;border:2px solid var(--coral);color:var(--ink);font-size:12px;font-weight:700;letter-spacing:2px;padding:10px 20px}

/* call to action */
.cta{height:129px;background:var(--coral)}
.cta .wrap{height:129px;display:flex;align-items:center;justify-content:space-between;padding:0 28px}
.cta h2{font-family:"Roboto Slab",serif;font-weight:300;font-size:29px;color:var(--white)}
.cta p{font-size:13px;color:#fbd4d2;margin-top:6px}
.cta .btn-light{padding:11px 20px;margin-right:6px}

/* footer widgets */
.footer-widgets{height:306px;background:var(--band)}
.footer-widgets .wrap{display:flex;padding:38px 27px 0}
.widget{width:302px}
.widget h4{font-size:13px;font-weight:700;color:var(--ink);margin-bottom:28px}
.widget p{font-size:12px;line-height:1.6;color:var(--ink);width:270px}
.widget p + p{margin-top:14px}
.handle{color:var(--coral)}
.search{margin-top:38px;width:272px;height:28px;border-radius:14px;background:var(--white);border:1px solid #ccc;font-size:12px;color:#888;padding:6px 14px}
.follow{display:flex;align-items:center;gap:8px;margin-top:14px;font-size:12px;color:var(--coral)}
.follow::before{content:"";width:12px;height:12px;border-radius:50%;background:#aaa}
.widget ul{margin-top:14px;padding-left:18px}
.widget ul li{list-style:disc;font-size:12px;line-height:2.2;color:var(--ink)}

/* footer bottom */
.footer-nav{height:50px;background:var(--white);border-top:1px solid var(--line);border-bottom:1px solid var(--line)}
.footer-nav .wrap{height:50px;display:flex;align-items:center;justify-content:space-between}
.footer-links{display:flex;gap:30px;font-size:12px;letter-spacing:1px;color:var(--ink)}
.copyright{height:75px;background:var(--band);text-align:center;font-size:10px;color:#999;padding-top:32px}
</style>
</head>
<body>

<header class="site-header">
  <div class="wrap">
    <a class="brand" href="#"><span class="brand-dot"></span>BrightNova</a>
    <nav class="main-nav">
      <a href="#">HOME</a><a href="#">BLOG</a><a href="#">SERVICE</a><a href="#">CLIENTS</a><a href="#">CONTACT</a>
      <a class="btn-signin" href="#">SIGNIN</a>
    </nav>
  </div>
</header>

<div class="subnav">
  <div class="wrap">
    <nav class="subnav-links"><a href="#">Home</a><a href="#">Blog</a><a href="#">Service</a><a href="#">Clients</a><a href="#">Portfolio</a></nav>
    <div class="social"><span></span><span></span><span></span><span></span><span></span><span></span></div>
  </div>
</div>

<section class="hero" role="img" aria-label="Night city skyline by the water with colourful fireworks bursting overhead">
  <div class="wrap">
    <div class="hero-box">
      <div class="hero-kicker">BRIGHTNOVA EVENTS</div>
      <h1 class="hero-title">Collab With Us</h1>
      <p class="hero-text">Quis aute iure reprehenderit in voluptate velit esse cillum dolore eu fugiat nulla pariatur.</p>
      <div class="hero-actions"><a class="btn-light" href="#">CONTACT</a><a class="btn-outline" href="#">ONLY $5000</a></div>
    </div>
  </div>
  <div class="hero-dots"><span class="on"></span><span></span><span></span><span></span><span></span></div>
</section>

<section class="features">
  <div class="wrap">
    <div class="feature">
      <div class="feature-icon" role="img" aria-label="Green clipboard checklist icon" style="background:#3cae5c"></div>
      <h3>Visible liquid droplets.</h3><div class="rule"></div>
      <p>Lorem ipsum dolor sit consect adip lacing elit laoreet dolore.</p>
      <a class="more" href="#">FLY HIGH</a>
    </div>
    <div class="feature">
      <div class="feature-icon" role="img" aria-label="Folded map icon" style="background:linear-gradient(135deg,#e9e9e9,#f2c14e 50%,#e35d4f)"></div>
      <h3>Depicts visual perception.</h3><div class="rule"></div>
      <p>Lorem ipsum dolor sit consect adip lacing elit laoreet dolore.</p>
      <a class="more" href="#">SOME LINK</a>
    </div>
    <div class="feature">
      <svg class="feature-icon" viewBox="0 0 82 82" aria-label="Speech bubbles icon" role="img">
        <rect x="18" y="6" width="52" height="40" rx="3" fill="#c0392b"/>
        <rect x="10" y="16" width="54" height="40" rx="3" fill="#e74c3c"/>
        <path d="M22 56 L22 70 L36 56 Z" fill="#e74c3c"/>
      </svg>
      <h3>Blast from the past.</h3><div class="rule"></div>
      <p>Lorem ipsum dolor sit consect adip lacing elit laoreet dolore.</p>
      <a class="more" href="#">TAKE OFF</a>
    </div>
  </div>
</section>

<section class="blog-area">
  <div class="wrap">
    <div class="blog-col">
      <h3 class="section-label">Latest From Our Blog <span class="plus"></span></h3>
      <ul class="post-list">
        <li>Could You Be Living Inside A Black Hole?</li>
        <li>Finding the Right Accommodation for a Rocky Mountain Vacation</li>
        <li>Direction Quote</li>
        <li>Spartacus Link</li>
        <li>Treasured Memories Of Vacations At The Beach</li>
      </ul>
    </div>
    <aside class="cat-col">
      <h4>Categories</h4>
      <ul>
        <li>» Entertainment <small>(5)</small></li>
        <li>» Food <small>(1)</small></li>
        <li>» Galleries <small>(2)</small></li>
        <li>» Music <small>(4)</small></li>
        <li>» Technology <small>(4)</small></li>
        <li>» Travel <small>(5)</small></li>
        <li>» Videos <small>(2)</small></li>
      </ul>
    </aside>
  </div>
</section>

<section class="projects">
  <div class="wrap">
    <h2>Recent Projects</h2><div class="rule"></div>
    <div class="project-strip">
      <div class="project-tile tile-a" role="img" aria-label="White firework burst against a night sky"></div>
      <div class="project-tile tile-b" role="img" aria-label="Red firework sparks against a night sky"></div>
      <div class="project-tile tile-a" role="img" aria-label="White firework burst against a night sky"></div>
      <div class="project-tile tile-b" role="img" aria-label="Red firework sparks against a night sky"></div>
    </div>
    <p>Lorem ipsum dolor sit amet, consectetur adipisicing elit, sed do eiusmod tempor incididunt ut labore et dolore magna aliqua.</p>
    <a class="btn-frame" href="#">RECENT PROJECTS</a>
  </div>
</section>

<section class="cta">
  <div class="wrap">
    <div>
      <h2>You should so check this out</h2>
      <p>Lorem ipsum dolor sit amet euismod ut laoreet dolore erat volutpat.</p>
    </div>
    <a class="btn-light" href="#">CHECK THIS</a>
  </div>
</section>

<footer>
  <div class="footer-widgets">
    <div class="wrap">
      <div class="widget">
        <h4>About Us</h4>
        <p>Lorem ipsum dolor sit amet, consectetuer adipiscing elit, sed diam nonummy nibh euismod tincidunt ut laoreet dolore magna aliquam erat volutpat.</p>
        <div class="search">Search here...</div>
      </div>
      <div class="widget">
        <h4>Latest Tweets</h4>
        <p><span class="handle">@lanterncode</span> Any plans to bring back the web version of comet? I would love to have my comet snaps browsable online somewhere.</p>
        <p>Get some awesomeness <span class="handle">@orbitlane</span> erat a ante venenatis dapibus posuere velit aliquet.</p>
        <a class="follow" href="#">Follow on Chirper</a>
      </div>
      <div class="widget">
        <h4>Hello There</h4>
        <p>Lorem ipsum dolor sit amet, consectetuer adipiscing elit, sed diam nonummy nibh euismod tincidunt ut laoreet dolore.</p>
        <ul><li>Lorem ipsum dolor elit.</li><li>Aliquam tincidunt mauris eu risus.</li><li>Vestibulum auctor neque.</li></ul>
      </div>
    </div>
  </div>
  <div class="footer-nav">
    <div class="wrap">
      <nav class="footer-links"><a href="#">Home</a><a href="#">Blog</a><a href="#">Services</a><a href="#">Clients</a><a href="#">Contact</a></nav>
      <div class="social"><span></span><span></span><span></span><span></span><span></span><span></span></div>
    </div>
  </div>
  <div class="copyright">Copyright ©</div>
</footer>

</body>
</html>
```